Webdesign für eine Metallfirma
Zielgruppe
Der Auftraggegeber ist eine Metallfirma, welche sich mit Metallbau, Parktechnik,Preßwerkzeugen,Stadtmöblierung
und neu mit Erneuerbaren Energien beschäftigt.
Zielgruppe sind sowohl private als auch geschäftliche Partner, aber auch Städte und Gemeinden.
Aufgabenstellung
- das Layout benötigen wir als PSD
- nur die Startseite soll gelayoutet werden
- die vorherrschende Farbe orientiert sich am Logo, gewünscht ist eine weitere Farbe, da verlassen wir uns auf Ihren Geschmack (siehe anbei)
- die Inhalte der beiden angegebenen Webseiten sollen zusammengeführt werden (siehe unten)
- bitte lassen Sie die Navigationspunkte in allen Ebenen aufklappen

```html
<!DOCTYPE html>
<html lang="de">
<head>
<meta charset="utf-8">
<title>NoRa – Startseite</title>
<link rel="stylesheet" href="https://fonts.googleapis.com/css2?family=PT+Sans:wght@400;700&family=Poppins:wght@400;500&display=swap">
<style>
:root{
  --blue:#3f8ad6;
  --ink:#444a50;
  --muted:#7d8389;
  --line:#e6e8ea;
  --paper:#ffffff;
  --bg:#ffffff;
}
*{margin:0;padding:0;box-sizing:border-box}
html,body{width:1200px;height:1200px;overflow:hidden;background:var(--bg)}
.stage{position:absolute;left:0;top:0;width:1920px;height:1920px;transform:scale(.625);transform-origin:0 0}
.page{position:absolute;left:675px;top:25px;width:557px;height:1895px;background:var(--paper);
  box-shadow:0 0 6px rgba(0,0,0,.18);font-family:"Poppins",sans-serif;color:var(--ink)}

.brand{position:absolute;left:8px;top:6px;display:flex;align-items:center;gap:6px}
.brand-mark{width:26px;height:26px;background:var(--blue)}
.brand-name{font-family:"PT Sans",sans-serif;font-weight:700;font-size:10.5px;line-height:12px;color:var(--blue);white-space:nowrap}
.top-contact{position:absolute;right:8px;top:4px;font-size:6px;font-style:italic;color:var(--blue);white-space:nowrap}

.main-nav{position:absolute;left:9px;top:55px;width:400px;height:10px;font-family:"PT Sans",sans-serif;font-weight:700;font-size:6.5px;color:#222}
.main-nav span{position:absolute;top:0;white-space:nowrap}
.main-nav .active{color:var(--blue)}

.photo{position:absolute;display:block}
.hero{left:0;top:75px;width:557px;height:231px;background:linear-gradient(110deg,#9a8c6e 0%,#c7b79a 35%,#8fa6c1 70%,#6f7f96 100%)}
.tile-solar{left:0;top:308px;width:128px;height:145px;background:linear-gradient(160deg,#f4f5f7,#dfe3ea 60%,#b9c2cf)}
.tile-card{left:130px;top:308px;width:427px;height:145px;background:linear-gradient(90deg,#c9c9c9 0%,#9b9b9b 45%,#4a4c50 80%,#3a3c40 100%)}

.cat-nav{position:absolute;left:0;top:453px;width:557px;height:45px;border-bottom:1px solid var(--line);font-family:"PT Sans",sans-serif;font-size:9px;color:#555;letter-spacing:.2px}
.cat-nav span{position:absolute;top:20px;white-space:nowrap}

.about-img{left:48px;top:553px;width:202px;height:141px;background:linear-gradient(180deg,#e6ebef 0%,#b7c0c8 45%,#3c4a5c 100%)}
.about-title{position:absolute;left:265px;top:553px;font-family:"PT Sans",sans-serif;font-weight:400;font-size:9px;color:#555;white-space:nowrap}
.about-text{position:absolute;left:265px;top:575px;width:258px;font-size:6px;line-height:9.8px;color:var(--muted)}
.btn-blue{position:absolute;left:265px;top:664px;width:106px;height:22px;background:var(--blue);color:#fff;font-size:6px;display:flex;align-items:center;justify-content:center}

.partner{position:absolute;left:0;top:752px;width:557px;text-align:center}
.partner h2{font-family:"PT Sans",sans-serif;font-weight:400;font-size:11.5px;color:#555}
.partner p{margin-top:8px;font-size:8.5px;line-height:11.5px;color:var(--muted)}
.section-label{position:absolute;left:0;top:841px;width:563px;text-align:center;font-family:"PT Sans",sans-serif;font-size:9.5px;color:#555}

.card-img{width:232px;height:124px}
.card-title{position:absolute;font-family:"PT Sans",sans-serif;font-weight:700;font-size:9.5px;color:#444;white-space:nowrap}
.card-text{position:absolute;width:225px;font-size:6px;line-height:9.8px;color:var(--muted)}
.img-metal{left:48px;top:892px;background:linear-gradient(135deg,#2a2c2e,#9da2a6 40%,#e3e5e7 60%,#5c6064)}
.img-park{left:292px;top:892px;background:linear-gradient(120deg,#1e56b0,#3a74c8 50%,#d7b08c 75%,#2b63b8)}
.img-press{left:48px;top:1114px;background:linear-gradient(120deg,#4a4642,#d8d6d2 40%,#eeeeec 70%,#c9c5bf)}
.img-bench{left:292px;top:1114px;background:linear-gradient(180deg,#4f7d3a,#8cb25e 60%,#6e9a48)}
.img-energy{left:48px;top:1329px;background:linear-gradient(180deg,#4d8fd6 0%,#a9cdee 45%,#2d4f8a 70%,#5c8f3c 100%)}

.contact-band{position:absolute;left:0;top:1546px;width:557px;height:92px;background:var(--blue);color:#fff}
.contact-band h3{position:absolute;left:30px;top:26px;font-family:"PT Sans",sans-serif;font-weight:700;font-size:9.5px;white-space:nowrap}
.contact-band p{position:absolute;left:30px;top:45px;width:345px;font-size:6px;line-height:8.6px}
.btn-outline{position:absolute;left:406px;top:49px;width:129px;height:24px;border:1px solid #fff;display:flex;align-items:center;justify-content:center;font-family:"PT Sans",sans-serif;font-weight:700;font-size:9px}

.staff-title{position:absolute;left:0;top:1670px;width:557px;text-align:center;font-family:"PT Sans",sans-serif;font-weight:700;font-size:9.5px;line-height:13.5px;color:#444}
.staff{position:absolute;top:1729px;font-size:5.2px;line-height:8.8px;color:#666;white-space:nowrap}
.staff b{display:block;font-weight:400;letter-spacing:.2px;margin-bottom:9px;color:#777}
.staff .name{display:block;margin-bottom:9px}

.footer{position:absolute;left:0;top:1825px;width:557px;border-top:1px solid var(--line);height:70px;font-size:4.8px;color:#777}
.footer span{position:absolute;white-space:nowrap}
</style>
</head>
<body>
<div class="stage">
  <div class="page">
    <header>
      <div class="brand"><span class="brand-mark"></span><span class="brand-name">NoRa Norder Metall-<br>und Anlagenbau GmbH</span></div>
      <div class="top-contact">Tel.: +49 (0) 12345 678-0 &nbsp; I &nbsp; E-Mail: info@nora-metall.de</div>
      <nav class="main-nav">
        <span class="active" style="left:0">HOME</span>
        <span style="left:44px">WER WIR SIND</span>
        <span style="left:102px">PRODUKTE</span>
        <span style="left:157px">KARRIERE</span>
        <span style="left:207px">AKTUELLES</span>
        <span style="left:260px">KONTAKT</span>
      </nav>
    </header>

    <div class="photo hero" role="img" aria-label="Foto: zwei lächelnde Mitarbeiter in der Werkhalle, einer mit Schutzhelm, einer mit Tablet"></div>
    <div class="photo tile-solar" role="img" aria-label="Foto: Straßenlaterne mit Solarmodul"></div>
    <div class="photo tile-card" role="img" aria-label="Foto: Hand steckt Karte in einen Parkautomaten"></div>

    <nav class="cat-nav">
      <span style="left:13px">METALLBAU</span>
      <span style="left:95px">PARKTECHNIK</span>
      <span style="left:185px">PRESSWERKZEUGE</span>
      <span style="left:303px">STADTMÖBLIERUNG</span>
      <span style="left:415px">ERNEUERBARE ENERGIEN</span>
    </nav>

    <section>
      <div class="photo about-img" role="img" aria-label="Foto: Team aus fünf Mitarbeitenden im Büro"></div>
      <h2 class="about-title">WER WIR SIND</h2>
      <p class="about-text">Lorem ipsum dolor sit amet, consectetuer adipiscing elit. Aenean commodo ligula eget dolor. Aenean massa. Cum sociis natoque penatibus et magnis dis parturient montes, nascetur ridiculus mus. Donec quam felis, ultricies nec, pellentesque eu, pretium quis, sem. Nulla consequat massa quis enim. Donec pede justo, fringilla vel, aliquet nec, vulputate eget, arcu. In enim justo, rhoncus ut, imperdiet a, venenatis vitae, justo. Nullam dictum felis eu pede mollis pretium. Integer tincidunt. Cras dapibus.</p>
      <div class="btn-blue">Mehr zum Unternehmen</div>
    </section>

    <section class="partner">
      <h2>NoRa - Ihr verlässlicher Partner</h2>
      <p>Wir sind im Metallbau,&nbsp; Parktechnik, Presswerkzeuge,<br>Stadtmöblierung und erneuerbare Energien tätig.<br>Lorem ipsum dolor sit amet, consectetuer adipising elit.</p>
    </section>
    <div class="section-label">Was wir tun</div>

    <div class="photo card-img img-metal" role="img" aria-label="Foto: gestapelte Metallprofile und Rohre"></div>
    <h3 class="card-title" style="left:51px;top:1019px">Metallbau</h3>
    <p class="card-text" style="left:51px;top:1037px">Herstellung von Metallbauerzeugnissen auf dem Gebiet der Verkehrsleit-, Absperr-, sowie der Werbetechnik, Anfertigung von Zäunen, Gittern, Toren, Geländern, Treppen u.v.m.</p>

    <div class="photo card-img img-park" role="img" aria-label="Foto: Hand mit Parkticket am Automaten"></div>
    <h3 class="card-title" style="left:292px;top:1019px">Parktechnik</h3>
    <p class="card-text" style="left:292px;top:1037px">Lieferung und Aufstellung von Parkscheinautomaten, Gebührenautomaten, Schrankenanlagen und kompletten Parksystemen, Polleranlagen sowie Personensperren (Vereinzelungsanlagen).</p>

    <div class="photo card-img img-press" role="img" aria-label="Foto: Handwerker verpresst Rohre mit einem Presswerkzeug"></div>
    <h3 class="card-title" style="left:50px;top:1244px">Presswerkzeuge</h3>
    <p class="card-text" style="left:50px;top:1261px">Cum sociis natoque penatibus et magnis dis parturient montes, nascetur ridiculus mus. Donec quam felis, ultricies nec,</p>

    <div class="photo card-img img-bench" role="img" aria-label="Foto: Parkbank im Grünen"></div>
    <h3 class="card-title" style="left:293px;top:1243px">Stadtmöblierung</h3>
    <p class="card-text" style="left:293px;top:1262px">Cum sociis natoque penatibus et magnis dis parturient montes, nascetur ridiculus mus. Donec quam felis, ultricies nec.</p>

    <div class="photo card-img img-energy" role="img" aria-label="Foto: Solarpark mit Windrädern unter blauem Himmel"></div>
    <h3 class="card-title" style="left:50px;top:1459px">Erneuerbare Energien</h3>
    <p class="card-text" style="left:50px;top:1476px">Cum sociis natoque penatibus et magnis dis parturient montes, nascetur ridiculus mus. Donec quam felis, ultricies nec,</p>

    <section class="contact-band">
      <h3>Sie haben Fragen? Wir beraten Sie gerne. Nehmen Sie Kontakt mit uns auf.</h3>
      <p>Lorem ipsum dolor sit amet, consectetuer adipiscing elit. Aenean commodo ligula eget dolor. Aenean massa. Cum sociis natoque penatibus et magnis dis parturient montes, nascetur ridiculus mus. Donec quam felis,</p>
      <div class="btn-outline">E-Mail schreiben</div>
    </section>

    <h2 class="staff-title">Unsere Ansprechpartner in den Fachbereichen stehen Ihnen gerne telefonisch<br>oder per E-Mail zur Verfügung</h2>
    <div class="staff" style="left:48px"><b>PARKTECHNIK</b><span class="name">Herr Berger</span>Telefon: +49 (0) 12345 678-114<br>E-Mail: b.berger@nora-metall.de</div>
    <div class="staff" style="left:159px"><b>METALLBAU</b><span class="name">Herr Lindner</span>Telefon: +49 (0) 12345 678-113<br>E-Mail: l.lindner@nora-metall.de</div>
    <div class="staff" style="left:272px"><b>SANITÄRTECHNIK &amp; ERNEUERBARE ENERGIEN</b><span class="name">Herr Vogt</span>Telefon: +49 (0) 12345 678-108<br>E-Mail: v.vogt@nora-metall.de</div>
    <div class="staff" style="left:416px"><b>GESCHÄFTSLEITUNG</b>Telefon: +49 (0) 12345 678-0<br>Telefax: +49 (0) 12345 678-130<br>E-Mail: &nbsp;info@nora-metall.de</div>

    <footer class="footer">
      <span style="left:13px;top:20px">NoRa Norder Metall- und Anlagenbau GmbH</span>
      <span style="left:164px;top:20px">Werkstraße 12 · 01234 Talheim</span>
      <span style="left:292px;top:20px">Tel.: +49 (0) 12345 678-0 &nbsp;I&nbsp; Fax: +49 (0) 12345 678-130</span>
      <span style="left:453px;top:19px">E-Mail: info@nora-metall.de</span>
      <span style="left:15px;top:48px">Datenschutz</span>
      <span style="left:59px;top:48px">Impressum</span>
      <span style="left:113px;top:47px">Copyright NoRa 2022</span>
    </footer>
  </div>
</div>
</body>
</html>
```